Family Owned Construction Company Needs Modern Business Cards

We need a new design for our business cards. We are a family owned construction company, Brantwell Construction, based in Mendon, Vermont and would like to add in our new logo and find a more modern look. We also want to use our old to make sure people know who we are. We do site development, highway, environmental, demolition, utility and aggregate.

Contact Information for Business Card

We want to have the office address, 418 Quarry Ridge Road, Fernhollow, FH 05788 and our phone (802) 555-0137 and fax (802) 555-0164 on there as well. Our website is www.brantwellinc.example. There should be a place for the person's name, title, cell number, and email address on the card. Words that we would like to be associated with our company are honesty, predictable, reliable, integrity, dedicated, built right quality, consistent, whatever it takes, and innovation. Safety is also very important to us.

Font styles to use
Serif
Sans Serif
Other font styles liked:
• Square 721 Extented

Colors
0255a3
ffffff

Requirements
Must have
• Office address, phone number and fax number. New logo with excavator
Nice to have
• That we do site development, highway, environmental, demolition, utility, and aggregate. Both logos

```html
<!DOCTYPE html>
<html lang="en">
<head>
<meta charset="utf-8">
<title>Brantwell Construction – Business Card</title>
<link rel="stylesheet" href="https://fonts.googleapis.com/css2?family=Open+Sans:wght@400;600;700&display=swap">
<style>
  :root {
    --stage: #000000;
    --card-light: #f2f2f2;
    --card-navy: #0b2d5c;
    --navy-faint: #1f4478;
    --brand-blue: #1f3c88;
    --ink: #222222;
    --white: #ffffff;
  }
  html, body {
    margin: 0;
    padding: 0;
    width: 1200px;
    height: 900px;
    overflow: hidden;
    background: var(--stage);
    font-family: "Open Sans", Arial, sans-serif;
  }
  .canvas {
    position: relative;
    width: 1200px;
    height: 900px;
  }
  .card {
    position: absolute;
    top: 200px;
    width: 310px;
    height: 502px;
    overflow: hidden;
  }
  .card-front {
    left: 293px;
    background: var(--card-light);
    border-radius: 60px 0 60px 0;
  }
  .card-back {
    left: 613px;
    width: 309px;
    background: var(--card-navy);
    border-radius: 0 60px 0 60px;
  }
  .front-mark {
    position: absolute;
    left: 72px;
    top: 100px;
    width: 210px;
    display: flex;
    align-items: center;
    gap: 10px;
    color: var(--brand-blue);
    font-weight: 700;
    font-size: 18px;
    line-height: 1.15;
  }
  .front-mark .mark-square {
    width: 26px;
    height: 26px;
    background: var(--brand-blue);
    flex: none;
  }
  .person {
    position: absolute;
    left: 26px;
    top: 287px;
  }
  .person-name {
    margin: 0;
    font-size: 16px;
    font-weight: 600;
    color: var(--brand-blue);
    line-height: 20px;
  }
  .person-title {
    margin: 0;
    font-size: 13px;
    color: var(--ink);
    line-height: 18px;
  }
  .address {
    position: absolute;
    left: 26px;
    top: 336px;
    margin: 0;
    font-size: 13px;
    line-height: 18px;
    color: var(--ink);
    font-style: normal;
  }
  .contact-list {
    position: absolute;
    left: 26px;
    top: 386px;
    margin: 0;
    padding: 0;
    list-style: none;
    font-size: 13px;
    color: var(--ink);
  }
  .contact-list li {
    display: flex;
    align-items: center;
    height: 18px;
  }
  .contact-list svg {
    width: 9px;
    height: 9px;
    margin-right: 9px;
    fill: var(--brand-blue);
  }
  .back-decoration {
    position: absolute;
    left: 60px;
    top: 30px;
    width: 249px;
    height: 262px;
    border-radius: 18px 60px 0 0;
    background: linear-gradient(160deg, var(--navy-faint), rgba(31, 68, 120, 0.35));
  }
  .back-mark {
    position: absolute;
    left: 26px;
    top: 372px;
    width: 262px;
    display: flex;
    align-items: center;
    gap: 10px;
    color: var(--white);
    font-weight: 700;
    font-size: 21px;
    line-height: 1.15;
  }
  .back-mark .mark-square {
    width: 30px;
    height: 30px;
    background: var(--white);
    flex: none;
  }
</style>
</head>
<body>
<main class="canvas">
  <section class="card card-front">
    <div class="front-mark">
      <span class="mark-square"></span>
      <span class="mark-name">Brantwell Construction Inc.</span>
    </div>

    <div class="person">
      <p class="person-name">Daniel Whitford</p>
      <p class="person-title">Managing Director</p>
    </div>

    <address class="address">418 Quarry Ridge Road, Fernhollow,<br>FH 05788</address>

    <ul class="contact-list">
      <li>
        <svg viewBox="0 0 10 10" aria-hidden="true"><path d="M3 0h4a1 1 0 0 1 1 1v8a1 1 0 0 1-1 1H3a1 1 0 0 1-1-1V1a1 1 0 0 1 1-1zm0 1.5v6h4v-6z"/></svg>
        (802) 555-0191
      </li>
      <li>
        <svg viewBox="0 0 10 10" aria-hidden="true"><path d="M0 3c2-2 8-2 10 0l-1 1.5-2-.5V3H3v1L1 4.5zM2 5h6l1 4H1z"/></svg>
        (802) 555-0137
      </li>
      <li>
        <svg viewBox="0 0 10 10" aria-hidden="true"><path d="M2 0h5v3H2zM0 3.5h10V10H0zm2 2v1h2v-1zm3 0v1h2v-1zm-3 2v1h2v-1zm3 0v1h2v-1z"/></svg>
        (802) 555-0164
      </li>
      <li>
        <svg viewBox="0 0 10 10" aria-hidden="true"><path d="M0 2h10v1L5 6 0 3zm0 2l5 3 5-3v4H0z"/></svg>
        info@brantwellinc.example
      </li>
      <li>
        <svg viewBox="0 0 10 10" aria-hidden="true"><circle cx="5" cy="5" r="4.5"/></svg>
        www.brantwellinc.example
      </li>
    </ul>
  </section>

  <section class="card card-back">
    <div class="back-decoration" role="img" aria-label="Faint large excavator silhouette in lighter navy"></div>
    <div class="back-mark">
      <span class="mark-square"></span>
      <span class="mark-name">Brantwell Construction Inc.</span>
    </div>
  </section>
</main>
</body>
</html>
```